Business Card/ Email Signature Design Project

I am an Interior Designer. I need a business card that looks sophisticated stylish but simple in design. My work covers space design/ interior architecture/ furniture design/ product development & styling.

I have a very specific brief and know mostly what I want. I'm hoping to work with someone who can translate my ideas.

My branding should have a strong focus on my name, the majority of my work is referral based.
I'm keen to keep a monochromatic colour scheme: dark charcoal/ black/ white/ embossing/ silver. I'm not suggesting we use all that I've listed, they are possible ideas at this stage. I will need to be mindful of printing costs an also how I make the design work across, cards, letter heads, email logo and web design.

Theory behind images sent below;
1-Rug Image_(minus boarder) I was thinking this image could be used on the back of the card with my contact details over. I like that the lines are almost hand drawn and start to look free form. It's a subtle contrast to a more formal front of the card with my name.
2_Owen Ratley_I really like the orientation, the proportion of font on the card, the colour and the font. I like the lower case for my name and the upper case for 'Interior Design'. Not sure if it should be 'Interior Designer or Interior Design' at this stage, was leaning towards 'Interior Design'. Was thinking the 'i' and 'd' in my surname could be the colour eg 'silver'?? We can decide on this once we see it.

Look forward to hearing from you.
Cheers,
Noreen Bastoli

Industry/Entity Type

Printing

Logo Text

Noreen Bastoli Interior Design

```html
<!DOCTYPE html>
<html lang="en">
<head>
<meta charset="utf-8">
<title>Noreen Bastoli — Interior Design business card</title>
<link rel="stylesheet" href="https://fonts.googleapis.com/css2?family=Didact+Gothic&family=Poppins:wght@600&display=swap">
<style>
  :root {
    --backdrop: #d6d6d4;
    --card-black: #050505;
    --charcoal: #1c1c1c;
    --band-grey: #4b4b4b;
    --panel-grey: #363636;
    --line-grey: #5a5a5a;
    --muted-grey: #6c6c6c;
    --silver-light: #bdbdbd;
    --silver-dark: #6f6f6f;
    --white: #ffffff;
  }
  * { box-sizing: border-box; margin: 0; padding: 0; }
  html, body {
    width: 1200px;
    height: 900px;
    overflow: hidden;
    background: var(--backdrop);
  }
  .sheet {
    width: 1200px;
    height: 900px;
    display: flex;
    flex-direction: column;
    align-items: center;
    justify-content: center;
    gap: 56px;
  }
  .card {
    width: 520px;
    height: 317px;
    display: block;
    box-shadow: 0 10px 26px rgba(0, 0, 0, 0.28);
  }
  .contact-line {
    font-family: "Didact Gothic", sans-serif;
    font-size: 14px;
    fill: var(--white);
    letter-spacing: 0.6px;
  }
  .postal-address {
    font-family: "Didact Gothic", sans-serif;
    font-size: 15px;
    fill: var(--white);
    letter-spacing: 2.4px;
  }
  .name-wordmark {
    font-family: "Poppins", sans-serif;
    font-weight: 600;
    font-size: 36px;
    fill: var(--white);
    letter-spacing: 0.5px;
  }
  .discipline {
    font-family: "Didact Gothic", sans-serif;
    font-size: 22px;
    fill: var(--muted-grey);
    letter-spacing: 5px;
  }
</style>
</head>
<body>
<main class="sheet">

  <!-- Back of card: contact details over textured field -->
  <svg class="card card-back" viewBox="0 0 520 317" xmlns="http://www.w3.org/2000/svg">
    <defs>
      <linearGradient id="silver-frame" x1="0" y1="0" x2="1" y2="1">
        <stop offset="0" stop-color="var(--silver-light)"/>
        <stop offset="0.5" stop-color="var(--silver-dark)"/>
        <stop offset="1" stop-color="var(--silver-light)"/>
      </linearGradient>
      <radialGradient id="rug-field" cx="0.5" cy="0.45" r="0.7">
        <stop offset="0" stop-color="#262626"/>
        <stop offset="1" stop-color="#0c0c0c"/>
      </radialGradient>
    </defs>
    <rect class="silver-border" width="520" height="317" fill="url(#silver-frame)"
          role="img" aria-label="Speckled silver textured border"/>
    <rect class="rug-texture" x="16" y="16" width="488" height="285" fill="url(#rug-field)"
          role="img" aria-label="Dark rug texture with fine free-form hand-drawn lines"/>
    <polygon class="accent-plane" points="205,88 355,88 330,100 180,100" fill="var(--band-grey)"/>
    <polygon class="accent-plane" points="215,180 365,180 340,194 190,194" fill="var(--band-grey)"/>
    <text class="contact-line" x="272" y="124" text-anchor="middle">0413 555 271</text>
    <text class="contact-line" x="272" y="146" text-anchor="middle">interiors@noreenbastoli.com</text>
    <text class="contact-line" x="272" y="168" text-anchor="middle">www.noreenbastoli.com</text>
    <text class="postal-address" x="122" y="272">P.O BOX 217 ELMWOOD VIC. 3094</text>
  </svg>

  <!-- Front of card: name band and discipline -->
  <svg class="card card-front" viewBox="0 0 520 317" xmlns="http://www.w3.org/2000/svg">
    <rect class="card-base" width="520" height="317" fill="var(--card-black)"/>
    <polygon class="side-panel" points="372,0 520,0 520,317 468,317" fill="var(--panel-grey)"/>
    <line class="fold-line" x1="78" y1="0" x2="150" y2="317" stroke="var(--line-grey)" stroke-width="1.5"/>
    <line class="fold-line" x1="372" y1="0" x2="468" y2="317" stroke="var(--line-grey)" stroke-width="1"/>
    <g class="name-band" transform="rotate(-24 0 262)">
      <rect x="-30" y="214" width="640" height="50" fill="var(--band-grey)"/>
      <text class="name-wordmark" x="42" y="252">noreen bastoli</text>
    </g>
    <text class="discipline" x="212" y="294">INTERIOR DESIGN</text>
  </svg>

</main>
</body>
</html>
```